KVO-Business Card Design

I need a modern, professional business card design that includes my logo as the main feature, maybe the entire background with the contact info overlaying or even contact info on the back and the logo full frontal

Neat and organized placement of contact information

Would like to see options in black and white

Target Market(s)

real estate Developers, Construction managers, business and home owners

Industry/Entity Type

Construction

Contact Information for Business Card

KVO Construction
Danny Ferrante
General Contractor

Office: 1-888-902-7315 Ext #1
Cell: 215-730-4162
Fax: 1-888-902-7315

Font styles to use
Serif

Requirements
Must have
• title
• office #
• cell #
• Email
• website
Nice to have
• fax

```html
<!DOCTYPE html>
<html lang="en">
<head>
<meta charset="utf-8">
<title>KVO Construction – Business Card</title>
<link href="https://fonts.googleapis.com/css2?family=PT+Sans:wght@400;700&display=swap" rel="stylesheet">
<style>
  :root {
    --page-bg: #e9e7e3;
    --card-white: #ffffff;
    --green-light: #8cc34c;
    --green-mid: #4aa346;
    --green-dark: #1f7a35;
    --green-band: #2e7d3a;
    --brand-green: #3a9a3e;
    --text-white: #ffffff;
    --text-soft: #eef6ea;
  }
  * { margin: 0; padding: 0; box-sizing: border-box; }
  html, body {
    width: 1200px; height: 900px; overflow: hidden;
    background: var(--page-bg);
    font-family: "PT Sans", Arial, sans-serif;
  }
  .canvas { position: relative; width: 1200px; height: 900px; }

  .card {
    position: absolute;
    background: var(--card-white);
    box-shadow: 0 6px 18px rgba(0,0,0,0.18);
    overflow: hidden;
  }

  /* Front card */
  .card-front { left: 77px; top: 34px; width: 589px; height: 364px; }
  .front-header { height: 156px; position: relative; }
  .brand-name {
    position: absolute; left: 32px; top: 46px;
    font-size: 46px; font-weight: 700; color: var(--brand-green);
    letter-spacing: 0.5px; line-height: 1;
  }
  .brand-name .brand-dot {
    display: inline-block; width: 14px; height: 14px;
    background: var(--brand-green); border-radius: 50%;
    margin-right: 12px; vertical-align: middle; position: relative; top: -4px;
  }
  .front-body {
    position: absolute; left: 0; top: 156px; width: 100%; height: 208px;
    background: linear-gradient(to bottom, var(--green-light) 0%, var(--green-mid) 45%, var(--green-dark) 100%);
    color: var(--text-white);
    padding: 12px 0 0 31px;
  }
  .person-name { font-size: 21px; font-weight: 700; line-height: 1.2; }
  .person-title { font-size: 15px; color: var(--text-soft); margin-top: 2px; }
  .contact-list { list-style: none; margin-top: 20px; }
  .contact-list li {
    font-size: 15px; line-height: 24.5px;
    display: flex; align-items: center;
  }
  .contact-list svg { width: 12px; height: 12px; margin-right: 10px; fill: var(--text-white); flex: none; }

  /* Back card */
  .card-back { left: 388px; top: 505px; width: 567px; height: 352px; }
  .back-band-top { height: 75px; background: var(--green-band); }
  .back-center {
    height: 200px; position: relative;
    display: flex; flex-direction: column; align-items: center; justify-content: center;
  }
  .back-brand {
    font-size: 52px; font-weight: 700; color: var(--brand-green); line-height: 1;
  }
  .back-brand .brand-square {
    display: inline-block; width: 16px; height: 16px; background: var(--brand-green);
    margin-right: 14px; vertical-align: middle; position: relative; top: -5px;
  }
  .back-band-bottom {
    height: 77px; background: var(--green-band);
    display: flex; align-items: center; justify-content: center;
  }
  .website {
    color: var(--text-white); font-size: 15px; letter-spacing: 4px;
  }
</style>
</head>
<body>
<div class="canvas">

  <section class="card card-front" aria-label="Business card front">
    <div class="front-header">
      <div class="brand-name"><span class="brand-dot"></span>KVO Construction</div>
    </div>
    <div class="front-body">
      <div class="person-name">Danny Ferrante</div>
      <div class="person-title">General Contractor</div>
      <ul class="contact-list">
        <li>
          <svg viewBox="0 0 12 12" aria-hidden="true"><path d="M2.4 0.6l2 2.2-1 1.3c.6 1.5 1.9 2.8 3.5 3.5l1.3-1 2.2 2-1 2.2C5 10.6 1.4 7 1.2 1.6z"/></svg>
          1-888-902-7315 Ext #1
        </li>
        <li>
          <svg viewBox="0 0 12 12" aria-hidden="true"><path d="M3 0h6a1 1 0 0 1 1 1v10a1 1 0 0 1-1 1H3a1 1 0 0 1-1-1V1a1 1 0 0 1 1-1zm.3 1.3v8h5.4v-8zM6 9.8a.7.7 0 1 0 0 1.4.7.7 0 0 0 0-1.4z"/></svg>
          215-730-4162
        </li>
        <li>
          <svg viewBox="0 0 12 12" aria-hidden="true"><path d="M3 0h5v3H3zM1 4h10a1 1 0 0 1 1 1v6a1 1 0 0 1-1 1H1a1 1 0 0 1-1-1V5a1 1 0 0 1 1-1zm5 2v1.5h4V6zm0 2.5V10h4V8.5zM1.5 6v4.5h3V6z"/></svg>
          1-888-902-7315
        </li>
        <li>
          <svg viewBox="0 0 12 12" aria-hidden="true"><path d="M0 2h12v1L6 7 0 3zM0 4.3l6 4 6-4V10H0z"/></svg>
          info@kvobuild.com
        </li>
      </ul>
    </div>
  </section>

  <section class="card card-back" aria-label="Business card back">
    <div class="back-band-top"></div>
    <div class="back-center">
      <div class="back-brand"><span class="brand-square"></span>KVO Construction</div>
    </div>
    <div class="back-band-bottom">
      <span class="website">www.kvobuild.com</span>
    </div>
  </section>

</div>
</body>
</html>
```